GLS biz card

We need a business card design for our new company based in Los Angeles called "Gold Lantern Studios". We develop film and television projects. We work with investors, financiers, film production companies, film distribution and sales companies as well as studios. We would like to incorporate our logo (see attached) on a two-sided card. We need to include: name and title, address, phone, email and company website.

Target Market(s)

Business, financial and studio clients

Industry/Entity Type

Business

Contact Information for Business Card

Two-sided. We are thinking of the logo on one side and the information on the back. Please feel free to be creative! Thanks.

Requirements
Must have
• Please include the following text information, excluding the "CAPS CATEGORY:" and please allow the ability for us to change the name, title and email address for each company employee):
• NAME & TITLE:
• Peter Dunmore
• Managing Partner
• COMPANY NAME:
• GOLD LANTERN STUDIOS (please use existing logo)
• COMPANY ADDRESS:
• KVT Arts Park
• 2480 Wexley Boulevard
• Arts Hall, 4th Floor
• Harbor Point, CA 90417
• COMPANY PHONE NUMBER:
• 310-555-4206
• COMPANY WEBSITE ADDRESS:
• www.goldlanternstudioshouse.com
• EMAIL ADDRESS: (only one per card)
• frank@goldlanternstudioshouse.com
• tizzy@goldlanternstudioshouse.com
• peter@goldlanternstudioshouse.com

```html
<!DOCTYPE html>
<html lang="en">
<head>
<meta charset="utf-8">
<title>Gold Lantern Studios – Business Card</title>
<link href="https://fonts.googleapis.com/css2?family=Exo+2:wght@400;600&display=swap" rel="stylesheet">
<style>
  :root {
    --canvas-bg: #ebebeb;
    --card-dark: #231f20;
    --card-blue: #2a86cc;
    --card-light: #ffffff;
    --text-light: #f4f6f8;
    --brand-cyan: #22a6dc;
    --orb-core: #1a9ec6;
    --orb-edge: #0a1a20;
    --shadow: rgba(0, 0, 0, 0.75);
  }
  html, body {
    margin: 0;
    padding: 0;
    width: 1200px;
    height: 1000px;
    overflow: hidden;
    background: var(--canvas-bg);
    font-family: "Exo 2", sans-serif;
  }
  .card {
    position: absolute;
    background: var(--card-dark);
    box-shadow: 16px 16px 14px var(--shadow);
  }
  .card--info {
    left: 316px;
    top: 129px;
    width: 551px;
    height: 323px;
    background: linear-gradient(90deg,
      var(--card-dark) 0%,
      var(--card-dark) 34%,
      #3b4047 64%,
      #5f7f9e 82%,
      var(--card-blue) 91%,
      #bcd8f1 96%,
      var(--card-light) 100%);
  }
  .card--logo {
    left: 316px;
    top: 525px;
    width: 548px;
    height: 321px;
  }
  .brand {
    position: absolute;
    display: flex;
    flex-direction: column;
    align-items: center;
  }
  .brand__orb {
    border-radius: 50%;
    background: radial-gradient(circle at 50% 50%, var(--orb-core) 0%, #0d5a72 55%, var(--orb-edge) 100%);
    border: 1px solid #000;
  }
  .brand__name {
    color: var(--brand-cyan);
    font-weight: 600;
    letter-spacing: 0.06em;
    white-space: nowrap;
  }
  .card--info .brand {
    left: 55px;
    top: 106px;
    width: 120px;
  }
  .card--info .brand__orb {
    width: 72px;
    height: 72px;
  }
  .card--info .brand__name {
    margin-top: 8px;
    font-size: 11px;
  }
  .card--logo .brand {
    left: 124px;
    top: 58px;
    width: 300px;
  }
  .card--logo .brand__orb {
    width: 132px;
    height: 132px;
  }
  .card--logo .brand__name {
    margin-top: 14px;
    font-size: 22px;
  }
  .contact {
    position: absolute;
    right: 50px;
    top: 48px;
    text-align: right;
    color: var(--text-light);
    font-size: 16.5px;
    line-height: 20px;
  }
  .contact p { margin: 0; }
  .contact strong { font-weight: 600; }
  .contact__group + .contact__group { margin-top: 36px; }
  .contact__web { margin-top: 20px !important; }
</style>
</head>
<body>
  <section class="card card--info">
    <div class="brand">
      <div class="brand__orb"></div>
      <div class="brand__name">GOLD LANTERN STUDIOS</div>
    </div>
    <div class="contact">
      <div class="contact__group">
        <p><strong>Peter Dunmore</strong></p>
        <p><strong>Director</strong></p>
        <p>peter@goldlanternstudioshouse.com</p>
      </div>
      <div class="contact__group">
        <p><strong>KVT Arts Park</strong></p>
        <p>2480 Wexley Boulevard</p>
        <p>Arts Hall, 4th Floor</p>
        <p>Harbor Point, CA 90417</p>
        <p>Phone: 310-555-4206</p>
        <p class="contact__web">www.goldlanternstudioshouse.com</p>
      </div>
    </div>
  </section>

  <section class="card card--logo">
    <div class="brand">
      <div class="brand__orb"></div>
      <div class="brand__name">GOLD LANTERN STUDIOS</div>
    </div>
  </section>
</body>
</html>
```